Construction company focused on concrete and shed construction.

We need to update our current business card for ridgeforgebuilds.com.au we would like an eye catching design with blue, grey and white incorporating our current logo.
Our company started off in concreting and due to varying factors we have expanded to include shed construction as well.
This has led to our current Logo looking a little out of place and somehow need to use the card to bring in the shed construction side of the business while not having to change current concrete look "KESTRO" logo as we already have this incorporated into our company clothing and are not willing to change this yet.
Photo image attached for inspiration/ visual reference of type of work, not to be used on final design.
Please no cheesy designs of men in hard hats and tools
Final design should demonstrate a modern and service focused company.

Target Market(s)

Farmers, Business owners, Developers, Architects, Commercial project delivery

Industry/Entity Type

Construction Company

Contact Information for Business Card

Kestro Constructions.
7b Harlow st
East Marrowvale Tas
03 62918873

Font styles to use
Other font styles liked:
• see font in logo

Colors
3176b5
b2b2b2

Requirements
Must have
• Easy to read font,
• good contrast between back ground and writing
Nice to have
• Modern and corporate look with a fun but professional image.
Should not have
• Comic images or shadow images of tools/ people.

```html
<!DOCTYPE html>
<html lang="en">
<head>
<meta charset="utf-8">
<title>Kestro Constructions – Business Card</title>
<link rel="stylesheet" href="https://fonts.googleapis.com/css2?family=Open+Sans:wght@400;600;700&display=swap">
<style>
  :root {
    --brand-blue: #3176b5;
    --brand-grey: #b2b2b2;
    --ink: #4a4d52;
    --card: #eeeeec;
    --stage: #3a3a3a;
  }
  * { box-sizing: border-box; margin: 0; padding: 0; }
  html, body { width: 1200px; height: 901px; overflow: hidden; }
  body {
    background: var(--stage);
    font-family: "Open Sans", Arial, sans-serif;
    position: relative;
  }
  .card {
    position: absolute;
    top: 290px;
    width: 540px;
    height: 320px;
    border-radius: 22px;
    background: var(--card);
    overflow: hidden;
  }
  .card--front { left: 40px; }
  .card--back { left: 620px; }

  .wall-texture {
    position: absolute; inset: 0;
    background: linear-gradient(160deg, #f6f6f4 0%, #e6e6e4 100%);
  }
  .paint-splash {
    position: absolute; left: 0; top: 0;
    width: 300px; height: 110px;
    background: radial-gradient(ellipse at 20% 0%, rgba(49,118,181,.55) 0%, rgba(49,118,181,.18) 45%, rgba(49,118,181,0) 75%);
  }
  .contact {
    position: absolute; left: 34px; top: 70px;
    color: var(--ink);
    font-size: 14px;
    line-height: 1.45;
  }
  .contact__name {
    color: var(--brand-blue);
    font-weight: 700;
    font-size: 22px;
    letter-spacing: .5px;
    line-height: 1.1;
  }
  .contact__role { font-size: 13px; margin-bottom: 6px; }
  .contact__company { color: var(--brand-blue); font-weight: 700; font-size: 15px; }
  .contact__row { display: flex; align-items: center; gap: 8px; }
  .contact__row svg { width: 13px; height: 13px; flex: none; }
  .contact__web b { color: var(--brand-blue); font-weight: 600; }
  .contact__lines { margin-top: 4px; }

  .badge {
    position: absolute; right: 40px; bottom: 40px;
    width: 160px; height: 160px;
    border-radius: 50%;
    background: rgba(178,178,178,.35);
    display: flex; align-items: center; justify-content: center;
  }
  .badge__name {
    color: var(--brand-blue);
    font-weight: 700;
    font-size: 26px;
    letter-spacing: 1px;
  }

  .back__brand {
    position: absolute; left: 0; right: 0; top: 90px;
    display: flex; align-items: center; justify-content: center; gap: 14px;
  }
  .back__mark {
    width: 30px; height: 30px; background: var(--brand-blue);
  }
  .back__name {
    color: var(--brand-blue);
    font-weight: 700;
    font-size: 58px;
    letter-spacing: 2px;
  }
  .back__web {
    position: absolute; left: 0; right: 0; top: 190px;
    text-align: center;
    color: var(--ink);
    font-size: 24px;
    letter-spacing: .5px;
  }
</style>
</head>
<body>
  <section class="card card--front">
    <div class="wall-texture" role="img" aria-label="White painted brick wall texture"></div>
    <div class="paint-splash" role="img" aria-label="Blue paint splatter across the top corner"></div>

    <div class="contact">
      <p class="contact__name">MARCUS DELANE</p>
      <p class="contact__role">Managing Director</p>
      <p class="contact__company">KESTRO GROUP</p>
      <p>7b Harlow st</p>
      <p>East Marrowvale Tas</p>
      <div class="contact__lines">
        <p class="contact__row">
          <svg viewBox="0 0 16 16"><path fill="#3176b5" d="M3 1h3l1.5 4-2 1.5a9 9 0 0 0 4 4L11 8.5l4 1.5v3a2 2 0 0 1-2 2A13 13 0 0 1 1 3a2 2 0 0 1 2-2z"/></svg>
          03 62918873
        </p>
        <p class="contact__row">
          <svg viewBox="0 0 16 16"><path fill="#3176b5" d="M3 1h3l1.5 4-2 1.5a9 9 0 0 0 4 4L11 8.5l4 1.5v3a2 2 0 0 1-2 2A13 13 0 0 1 1 3a2 2 0 0 1 2-2z"/></svg>
          1300 4 KESTRO
        </p>
        <p class="contact__row">
          <svg viewBox="0 0 16 16"><rect x="1" y="3" width="14" height="10" rx="1" fill="#3176b5"/><path d="M1.5 3.5 8 9l6.5-5.5" stroke="#fff" stroke-width="1.3" fill="none"/></svg>
          admin@ridgeforgebuilds.com.au
        </p>
        <p class="contact__row contact__web">
          <svg viewBox="0 0 16 16"><circle cx="8" cy="8" r="7" fill="#3176b5"/><path d="M1 8h14M8 1c-3 3.5-3 10.5 0 14M8 1c3 3.5 3 10.5 0 14" stroke="#fff" stroke-width="1" fill="none"/></svg>
          <span>www.<b>ridgeforgebuilds</b>.com.au</span>
        </p>
      </div>
    </div>

    <div class="badge">
      <span class="badge__name">KESTRO</span>
    </div>
  </section>

  <section class="card card--back">
    <div class="back__brand">
      <span class="back__mark"></span>
      <span class="back__name">KESTRO</span>
    </div>
    <p class="back__web">ridgeforgebuilds.com.au</p>
  </section>
</body>
</html>
```